hello! I need a very simple modern business card for a new venture called The Quiet Harbor Retreats. It's the very first Tech-Free retreat in Asia!

The concept is very unique. Basically a group of 12-15 people would go on a 3 to 4 days retreat where no phone or internet is allowed. The first retreat will take place in a beautiful villa in Bali by the sea. It will include yoga, meditation, art & writing workshops, swimming, hiking, cooking, healthy vegetarian meals, etc.

Reason: Thanks for your submissions. I still haven't found exactly what I'm after but the designs that haven't be eliminated are getting close.. Please keep in mind that it should be a simple, modern and upmarket business card. Thanks

Target Market(s)

Both men and women who would like to disconnect from life, computer and phone for 3/4 days. They can be either local or expats but based in Asia (Singapore, Hong Kong).
Client will have to pay for their own flight and then the price is around US$600 for a 3-day retreat including everything (accommodation, food, activities). It means clients already have a good income. They are usually working in marketing, advertising, digital media, public relations.

Industry/Entity Type

Internet

Font styles to use
Other font styles liked:
• anything modern you like

Colors
acd036
9bcb3c
f37022
f68d4d
1b1b1b
333333
acd037

Requirements
Must have
• Name: Lina Vorel
Position: #gadgetdevotee
Company: The Quiet Harbor Retreats (asia should be smaller than the rest)
- Email button - quietharborretreats@mailverra.com
- FriendSpace button - www.friendspace.com/quietharborretreats
- TicketNest button - www.quietharborretreats.ticketnest.com
Nice to have
• You can use my logo attached but it's something I designed quickly on Power Point so it would be nice to include your own version.
Should not have
• anything tacky or girly or childish. thanks

```html
<!DOCTYPE html>
<html lang="en">
<head>
<meta charset="utf-8">
<title>The Quiet Harbor Retreats – Business Card</title>
<link rel="stylesheet" href="https://fonts.googleapis.com/css2?family=Orbitron:wght@800&family=Open+Sans:wght@400;600&display=swap">
<style>
  :root {
    --card-green: #9bcb3c;
    --card-green-deep: #7fb02a;
    --ink: #1b1b1b;
    --ink-soft: #333333;
    --paper: #ffffff;
    --backdrop: #8a8a8a;
    --backdrop-dark: #4a4a4a;
  }
  * { box-sizing: border-box; margin: 0; padding: 0; }
  html, body { width: 1200px; height: 900px; overflow: hidden; }
  body {
    background: linear-gradient(135deg, var(--backdrop) 0%, var(--backdrop-dark) 100%);
    position: relative;
    font-family: "Open Sans", Arial, sans-serif;
  }
  .card {
    position: absolute;
    width: 560px;
    height: 320px;
    background: var(--card-green);
    border-radius: 18px;
    box-shadow: 0 10px 30px rgba(0,0,0,0.25);
    overflow: hidden;
  }
  .card--front { left: 110px; top: 110px; }
  .card--back { left: 530px; top: 480px; }

  .wordmark {
    font-family: "Orbitron", "Arial Black", sans-serif;
    font-weight: 800;
    text-transform: uppercase;
    letter-spacing: 0.5px;
    line-height: 1.1;
  }
  .card--front .wordmark {
    position: absolute;
    left: 40px; right: 40px; top: 120px;
    color: var(--paper);
    font-size: 30px;
    text-align: right;
  }

  .card--back .wordmark {
    position: absolute;
    right: 26px; top: 28px;
    color: var(--ink);
    font-size: 22px;
    text-align: right;
  }
  .brand-ring {
    position: absolute;
    left: 22px; top: 110px;
    width: 180px; height: 180px;
  }
  .holder {
    position: absolute;
    right: 30px; top: 150px;
    text-align: right;
  }
  .holder__name {
    font-family: "Orbitron", "Arial Black", sans-serif;
    font-weight: 800;
    font-size: 17px;
    color: var(--paper);
    text-transform: uppercase;
  }
  .holder__role {
    font-size: 11px;
    color: var(--ink);
    margin-top: 3px;
  }
  .contacts {
    position: absolute;
    left: 228px; top: 200px;
    list-style: none;
  }
  .contacts li {
    display: flex;
    align-items: center;
    gap: 9px;
    font-size: 12.5px;
    color: var(--ink-soft);
    height: 22px;
  }
  .contacts svg { width: 14px; height: 14px; flex: none; }
</style>
</head>
<body>

<section class="card card--front" aria-label="Card front">
  <h1 class="wordmark">The Quiet Harbor Retreats</h1>
</section>

<section class="card card--back" aria-label="Card back">
  <h2 class="wordmark">The Quiet Harbor Retreats</h2>

  <svg class="brand-ring" viewBox="0 0 180 180" aria-hidden="true">
    <circle cx="90" cy="90" r="74" fill="none" stroke="var(--card-green-deep)" stroke-width="20"/>
  </svg>

  <div class="holder">
    <p class="holder__name">Lina Vorel</p>
    <p class="holder__role">#gadgetdevotee</p>
  </div>

  <ul class="contacts">
    <li>
      <svg viewBox="0 0 14 14" aria-hidden="true">
        <rect width="14" height="14" rx="3" fill="var(--paper)"/>
        <rect x="4.5" y="2.5" width="5" height="9" rx="1" fill="none" stroke="var(--card-green-deep)" stroke-width="1.2"/>
      </svg>
      0198 765 432
    </li>
    <li>
      <svg viewBox="0 0 14 14" aria-hidden="true">
        <rect width="14" height="14" rx="3" fill="var(--paper)"/>
        <rect x="3" y="4" width="8" height="6" fill="none" stroke="var(--card-green-deep)" stroke-width="1.1"/>
        <path d="M3 4 L7 7.5 L11 4" fill="none" stroke="var(--card-green-deep)" stroke-width="1.1"/>
      </svg>
      quietharborretreats@mailverra.com
    </li>
    <li>
      <svg viewBox="0 0 14 14" aria-hidden="true">
        <rect width="14" height="14" rx="3" fill="var(--paper)"/>
      </svg>
      /quietharborretreats
    </li>
    <li>
      <svg viewBox="0 0 14 14" aria-hidden="true">
        <rect width="14" height="14" rx="3" fill="var(--paper)"/>
      </svg>
      www.quietharborretreats.ticketnest.com
    </li>
  </ul>
</section>

</body>
</html>
```